Business Card Design Project

We need a business card for a chiropractic and rehabilitation center. We already have a logo and need the card to follow the color and feel of the logo.

Target Market(s)

adults 30-55 that have some ache or pain that is interfering with their life, so much as they are ready to do something about it.

Industry/Entity Type

Business

```html
<!DOCTYPE html>
<html lang="en">
<head>
<meta charset="UTF-8">
<title>Northbend Wellness – Business Card</title>
<link rel="stylesheet" href="https://fonts.googleapis.com/css2?family=Source+Sans+3:ital,wght@0,400;0,600;0,700;1,700&display=swap">
<style>
  :root {
    --backdrop: #3b4041;
    --card: #ffffff;
    --ink: #3d3d3d;
    --ink-soft: #4a4a4a;
    --brand-grey: #555759;
    --accent: #f5942a;
    --band-light: #6a6a6a;
    --band-dark: #414141;
    --on-band: #ffffff;
  }
  * { margin: 0; padding: 0; box-sizing: border-box; }
  html, body {
    width: 987px; height: 1200px; overflow: hidden;
    background: var(--backdrop);
    font-family: "Source Sans 3", "Myriad Pro", sans-serif;
  }
  .card {
    position: absolute;
    width: 790px; height: 450px;
    background: var(--card);
    border-radius: 28px;
    overflow: hidden;
  }
  .card--front { left: 86px; top: 95px; }
  .card--back  { left: 92px; top: 637px; }

  .brand {
    position: absolute; left: 0; right: 0;
    text-align: center;
    font-weight: 600; font-size: 48px; letter-spacing: 1px;
    color: var(--brand-grey); line-height: 1;
  }
  .card--front .brand { top: 106px; }
  .card--back .brand  { top: 169px; }

  .contact {
    position: absolute; left: 0; right: 0; top: 244px;
    text-align: center; color: var(--ink);
    font-size: 21px; line-height: 32.5px;
  }
  .contact b { font-style: italic; font-weight: 700; }
  .contact .sep { margin: 0 6px; }

  .band { position: absolute; left: 0; top: 0; width: 790px; height: 450px; }
  .holder {
    position: absolute; left: 0; right: 0; top: 396px;
    text-align: center; color: var(--on-band); font-size: 22px;
  }
  .holder strong { font-weight: 700; font-size: 26px; }

  .web {
    position: absolute; left: 0; right: 0; top: 354px;
    text-align: center; color: var(--ink-soft); font-size: 38px;
  }
</style>
</head>
<body>
  <section class="card card--front">
    <p class="brand">Northbend Wellness</p>
    <div class="contact">
      <p><b>t</b> : 123-123-1234 <span class="sep">|</span> <b>c</b> : 123-123-1234</p>
      <p><b>e</b> : info@website.com <span class="sep">|</span> <b>w</b>: www.website.com</p>
      <p>123 Street, Suit #123, Your City, State 12345</p>
    </div>
    <svg class="band" viewBox="0 0 790 450" aria-hidden="true">
      <defs>
        <linearGradient id="bandFill" x1="0" x2="1" y1="0" y2="0">
          <stop offset="0" stop-color="var(--band-light)"/>
          <stop offset="1" stop-color="var(--band-dark)"/>
        </linearGradient>
      </defs>
      <path d="M0 392 Q395 335 790 392 L790 401 Q395 344 0 401 Z" fill="var(--accent)"/>
      <path d="M0 406 Q395 350 790 406 L790 450 L0 450 Z" fill="url(#bandFill)"/>
    </svg>
    <p class="holder"><strong>Your Name,</strong> Designation</p>
  </section>

  <section class="card card--back">
    <p class="brand">Northbend Wellness</p>
    <p class="web">www.website.com</p>
  </section>
</body>
</html>
```